Develop a Corporate Identity for Q-LumaGridweb.com (Logo, Business Card & Letterhead)

Hi,

This is a sealed contest, we will guarantee this contest once we have some serious freelancers participate and receive some appealing designs.

Q-Luma Grid Solutions is an IT based company, which focusing on different needs in IT industries such as IT Consultancy, Design, Hosting & Networking. We need to design our Corporate Identity (Logo, Business Card & Letterhead)

Our domain name is Q-LumaGridweb.com, which is currently under development.

A Corporate ID (or Corporate Identity) must contain the key elements that are necessary to establish a professional looking brand for our business. The items included within a Corporate ID set include:
+ A logo
+ Business card
+ Company letterhead

Logo
The logo should be simple, elegant, clean and look classy.
It needs to be professional and eye catching.

Business Card
The card will be double sided with following detail appear.
(Company Name, Name, Phone number, Email address, Website URL)

Letterhead
Design should be matching color theme of Logo/Business card.

Templates (For business card & Letterhead)
Have attached design templates for your design in Adobe Illustrator format.
You must DELETE all GUIDE DESCRIPTIONS/TEXT INSTRUCTIONS.

Please don't feel restricted in your concepts by what we have provided in sample logo / name card design document.

We need the files to be delivered in .AI format (high quality vector), EPS, png, jpg formats and ready for printing!

Please make some suggestions for a nice design for the Corporate Identity.

By Googling Q-Luma/QLuma images, you may be seeing lots of different type of Q-LUMA logo, please note we are different from those industries and hence do not clone/copy those design idea. We need something that unique, identical and look professional.

Thank you in advance and we look forward to working with you.

```html
<!DOCTYPE html>
<html lang="en">
<head>
<meta charset="utf-8">
<title>Q-Luma Grid Solutions — Business Card</title>
<link rel="stylesheet" href="https://fonts.googleapis.com/css2?family=Mulish:wght@400;700&family=Arimo:wght@400;700&display=swap">
<style>
  :root {
    --backdrop: #141414;
    --card: #050505;
    --card-edge: #1e1e1e;
    --glow: #ffffff;
    --logo-ink: #1b1b1b;
    --accent: #f08a1c;
    --muted: #9a9a9a;
    --soft: #c8c8c8;
    --white: #ffffff;
  }
  * { margin: 0; padding: 0; box-sizing: border-box; }
  html, body { width: 1200px; height: 804px; overflow: hidden; background: var(--backdrop); }
  .canvas { position: relative; width: 1200px; height: 804px; background: var(--backdrop); }

  .card {
    position: absolute;
    width: 308px;
    height: 507px;
    border-radius: 21px;
    background: linear-gradient(180deg, #0c0c0c 0%, var(--card) 60%, #0a0a0a 100%);
    border: 1px solid var(--card-edge);
    overflow: hidden;
  }
  .card--front { left: 269px; top: 129px; }
  .card--back  { left: 619px; top: 136px; }

  .tagline {
    position: absolute;
    font-family: "Mulish", sans-serif;
    font-weight: 400;
    color: var(--muted);
    white-space: nowrap;
  }

  .glow { position: absolute; }
  .card--front .glow {
    left: 0; top: 196px; width: 308px; height: 142px;
    background: radial-gradient(ellipse 78% 50% at 70% 50%, var(--glow) 0%, rgba(255,255,255,0.85) 35%, rgba(255,255,255,0.25) 70%, rgba(255,255,255,0) 100%);
  }
  .card--back .glow {
    left: 0; top: 36px; width: 210px; height: 108px;
    background: radial-gradient(ellipse 62% 48% at 40% 50%, var(--glow) 0%, rgba(255,255,255,0.8) 35%, rgba(255,255,255,0.2) 72%, rgba(255,255,255,0) 100%);
  }

  .brand {
    position: absolute;
    display: flex;
    align-items: center;
    font-family: "Mulish", sans-serif;
    font-weight: 700;
    color: var(--logo-ink);
    white-space: nowrap;
    line-height: 1;
  }
  .brand__mark { display: inline-block; background: var(--accent); }

  .card--front .tagline { left: 24px; top: 152px; font-size: 26px; }
  .card--front .brand { left: 40px; top: 240px; font-size: 52px; gap: 12px; }
  .card--front .brand__mark { width: 30px; height: 30px; }

  .card--back .brand { left: 28px; top: 76px; font-size: 26px; gap: 7px; }
  .card--back .brand__mark { width: 15px; height: 15px; }
  .card--back .tagline { left: 165px; top: 78px; font-size: 16px; }

  .contact {
    position: absolute;
    left: 47px; top: 340px;
    padding-left: 12px;
    border-left: 1.5px solid var(--soft);
    font-family: "Arimo", sans-serif;
    font-size: 13px;
    line-height: 25px;
  }
  .contact__line { color: var(--muted); }
  .contact__line--handle { color: var(--white); font-weight: 700; }

  .website {
    position: absolute;
    left: 59px; top: 467px;
    font-family: "Arimo", sans-serif;
    font-size: 13px;
    font-weight: 700;
    color: var(--white);
  }
</style>
</head>
<body>
<main class="canvas">
  <section class="card card--front" aria-label="Business card front">
    <p class="tagline">Network Solutions</p>
    <div class="glow" aria-hidden="true"></div>
    <div class="brand"><span class="brand__mark"></span>Q-Luma</div>
  </section>

  <section class="card card--back" aria-label="Business card back">
    <div class="glow" aria-hidden="true"></div>
    <div class="brand"><span class="brand__mark"></span>Q-Luma</div>
    <p class="tagline">Network Solutions</p>
    <div class="contact">
      <p class="contact__line">0400 00555 123</p>
      <p class="contact__line">qluma@Q-LumaGridweb.com</p>
      <p class="contact__line contact__line--handle">Q-LumaGrid</p>
    </div>
    <p class="website">www.Q-LumaGridweb.com</p>
  </section>
</main>
</body>
</html>
```